Long term design collaboration - mobile app design & web app design

We are looking for a talented mobile designer to help us improve our UI & UX for mobile app and web app.

The screens that need to be redesigned are attached.

There is potentially a lot more work in future design available for the successful candidate.
The successful candidate would have to take part in daily stand-up around 3 times per week.
The successful candidate would join a dev team
We are software company that does property management

```html
<!DOCTYPE html>
<html lang="en">
<head>
<meta charset="utf-8">
<title>Holma – property management app screens</title>
<link rel="stylesheet" href="https://fonts.googleapis.com/css2?family=Poppins:wght@400;500;600;700&display=swap">
<style>
:root{
  --stage:#6b6b6b;
  --orange:#f7a100;
  --orange-soft:#fff7ea;
  --ink:#1d1d1d;
  --muted:#8a8a8a;
  --line:#e8e8e8;
  --white:#ffffff;
}
*{box-sizing:border-box;margin:0;padding:0}
html,body{width:1200px;height:762px;overflow:hidden}
body{background:var(--stage);font-family:"Poppins",sans-serif;color:var(--ink);position:relative}
.screen{position:absolute;top:92px;width:396px;height:820px;background:var(--white);border-radius:44px;overflow:hidden;transform:scale(.7055);transform-origin:0 0}
.screen--setup{left:102px}
.screen--finances{left:462px}
.screen--legionella{left:821px}
.abs{position:absolute}
.status{top:12px;left:32px;right:30px;height:20px;font-size:13px;font-weight:600;display:flex;justify-content:space-between;align-items:center}
.status__icons{display:flex;gap:4px;align-items:center}
.brand{top:44px;left:0;right:0;text-align:center;color:var(--orange);font-weight:700;font-size:16px;letter-spacing:.5px}
.rule{top:77px;left:32px;width:335px;height:1px;background:var(--line)}
.page-title{top:89px;left:0;right:0;text-align:center;font-size:13.5px;font-weight:600;letter-spacing:.2px}
.back{top:91px;left:30px}
/* setup */
.setup-panel{top:120px;left:13px;width:372px;height:90px;background:var(--orange-soft)}
.setup-field{width:161px;height:26px;background:var(--white);border:1px solid var(--line);font-size:8px;color:var(--muted);display:flex;align-items:center;padding-left:6px}
.setup-field::after{content:"";position:absolute;right:0;top:-1px;width:13px;height:26px;background:var(--orange)}
.setup-field svg{position:absolute;right:2px;top:8px;z-index:1}
.tabs{top:226px;left:93px;width:214px;height:31px;border:1px solid var(--line);border-radius:16px;background:var(--white);font-size:11.5px}
.tab{position:absolute;top:3px;height:24px;width:100px;border-radius:12px;display:flex;align-items:center;justify-content:center}
.tab--active{left:4px;background:var(--orange);color:var(--white)}
.tab--idle{left:110px}
.summary{top:276px;left:32px;width:335px;border:1px solid var(--line);background:var(--white)}
.summary__row{display:flex;border-bottom:1px solid var(--line);align-items:center;position:relative}
.summary__row:last-child{border-bottom:none}
.summary__label{width:108px;font-size:9.5px;padding-left:10px;border-right:1px solid var(--line);align-self:stretch;display:flex;align-items:center}
.summary__value{flex:1;font-size:8px;color:var(--muted);padding-left:8px}
.summary__go{width:31px;border-left:1px solid var(--line);align-self:stretch;display:flex;align-items:center;justify-content:center}
.modules{top:436px;left:13px;width:372px;height:330px;background:var(--orange-soft)}
.module-head{width:86px;text-align:center;font-size:9.5px;color:var(--orange)}
.module-head svg{display:block;margin:0 auto 6px}
.tile{width:76px;height:42px;background:var(--white);border:1px solid #f1ece4;text-align:center;font-size:8.5px;padding-top:8px;line-height:1.3}
.tile small{display:block;font-size:6.5px;color:var(--muted)}
.tile--tall{padding-top:3px}
/* tables */
.band{left:31px;width:334px;height:27px;background:var(--orange);color:var(--white);font-size:10px;font-weight:500;display:flex;align-items:center;justify-content:center}
.rows{left:31px;width:334px;background:var(--white);box-shadow:0 1px 4px rgba(0,0,0,.12)}
.row{height:37px;border-bottom:1px solid var(--line);display:flex;align-items:center;font-size:9px;position:relative;padding-left:10px}
.row:last-child{border-bottom:none}
.row__amt{position:absolute;left:157px;color:var(--orange);font-size:9.5px}
.row__total{position:absolute;left:211px;color:var(--muted);font-size:7.5px}
.row__count{position:absolute;left:267px;color:var(--orange);font-size:9.5px}
.row__unit{position:absolute;left:286px;color:var(--muted);font-size:7.5px}
.check{position:absolute;right:10px;width:9px;height:9px;border:1px solid #f3b34a;border-radius:1px}
.btn{top:309px;width:89px;height:29px;border-radius:15px;font-size:11.5px;font-weight:500;display:flex;align-items:center;justify-content:center}
.btn--ghost{left:105px;border:1.5px solid var(--orange);color:var(--orange);background:var(--white)}
.btn--solid{left:204px;background:var(--orange);color:var(--white)}
.art{top:380px;left:25px;width:350px;height:320px;border-radius:12px;background:radial-gradient(circle at 50% 50%,#f3f3f3 0%,#fdf3e0 45%,#ffffff 80%)}
/* nav */
.tabbar{top:758px;left:13px;width:372px;height:62px;background:var(--orange);border-radius:20px 20px 0 0;display:flex;justify-content:space-around;padding:10px 6px 0}
.tabbar__item{color:var(--white);font-size:12.5px;font-weight:500;text-align:center;width:86px}
.tabbar__item svg{display:block;margin:0 auto 2px}
.tabbar__item--home{color:#7a5a1c}
</style>
</head>
<body>

<!-- Screen 1: basic setup -->
<section class="screen screen--setup">
  <div class="abs status"><span>12:00</span><span class="status__icons"><svg width="58" height="11"><rect x="0" y="7" width="3" height="4" fill="#111"/><rect x="5" y="5" width="3" height="6" fill="#111"/><rect x="10" y="3" width="3" height="8" fill="#111"/><rect x="15" y="1" width="3" height="10" fill="#111"/><path d="M23 4 q6-5 12 0 M25 7 q4-3 8 0" stroke="#111" stroke-width="1.8" fill="none"/><rect x="38" y="1" width="18" height="9" rx="2" fill="#111"/></svg></span></div>
  <div class="abs brand">HOLMA</div>
  <div class="abs rule"></div>
  <div class="abs page-title">PLEASE COMPLETE BASIC SETUP</div>

  <div class="abs setup-panel"></div>
  <div class="abs setup-field" style="top:135px;left:32px">Service Charge Schedules<svg width="9" height="9"><circle cx="4.5" cy="4.5" r="4" fill="#fff"/><path d="M3.5 2.5l2 2-2 2" stroke="#f7a100" fill="none"/></svg></div>
  <div class="abs setup-field" style="top:135px;left:203px">Service Charge Appotionment<svg width="9" height="9"><circle cx="4.5" cy="4.5" r="4" fill="#fff"/><path d="M3.5 2.5l2 2-2 2" stroke="#f7a100" fill="none"/></svg></div>
  <div class="abs setup-field" style="top:168px;left:32px">Invite Residents&amp;Leaseholders<svg width="9" height="9"><circle cx="4.5" cy="4.5" r="4" fill="#fff"/><path d="M3.5 2.5l2 2-2 2" stroke="#f7a100" fill="none"/></svg></div>
  <div class="abs setup-field" style="top:168px;left:203px">Connect Payment Provider<svg width="9" height="9"><circle cx="4.5" cy="4.5" r="4" fill="#fff"/><path d="M3.5 2.5l2 2-2 2" stroke="#f7a100" fill="none"/></svg></div>

  <div class="abs tabs"><div class="tab tab--active">SUMMARY</div><div class="tab tab--idle">DETAILS</div></div>

  <div class="abs summary">
    <div class="summary__row" style="height:31px"><div class="summary__label">UNITS</div><div class="summary__value">85</div><div class="summary__go"><svg width="10" height="10"><circle cx="5" cy="5" r="5" fill="#f7a100"/><path d="M4 3l2 2-2 2" stroke="#fff" fill="none"/></svg></div></div>
    <div class="summary__row" style="height:39px"><div class="summary__label">HANDOVER DATE</div><div class="summary__value">12 January 2023</div><div class="summary__go"><svg width="10" height="10"><circle cx="5" cy="5" r="5" fill="#f7a100"/><path d="M4 3l2 2-2 2" stroke="#fff" fill="none"/></svg></div></div>
    <div class="summary__row" style="height:35px"><div class="summary__label">ADDRESS</div><div class="summary__value">42 Elmstead Row,London,N4 2QP</div><div class="summary__go"><svg width="10" height="10"><circle cx="5" cy="5" r="5" fill="#f7a100"/><path d="M4 3l2 2-2 2" stroke="#fff" fill="none"/></svg></div></div>
    <div class="summary__row" style="height:36px"><div class="summary__label">SECTION 20 LIMIT</div><div class="summary__value">$20</div><div class="summary__go"></div></div>
  </div>

  <div class="abs modules"></div>
  <div class="abs module-head" style="top:448px;left:27px"><svg width="20" height="22"><rect x="3" y="1" width="13" height="18" rx="1" fill="none" stroke="#f7a100" stroke-width="2"/><path d="M6 6h7M6 10h7M6 14h4" stroke="#f7a100" stroke-width="1.5"/></svg>Compliance</div>
  <div class="abs module-head" style="top:448px;left:113px"><svg width="22" height="22"><path d="M3 14 q8-10 16 0z" fill="#f7a100"/><path d="M11 14v5" stroke="#f7a100" stroke-width="2"/><path d="M2 19h18" stroke="#f7a100" stroke-width="2"/></svg>Insurances</div>
  <div class="abs module-head" style="top:448px;left:198px"><svg width="22" height="22"><circle cx="11" cy="7" r="6" fill="#f7a100"/><text x="11" y="10" font-size="8" fill="#fff" text-anchor="middle" font-family="Poppins,sans-serif">$</text><path d="M2 17 q6-3 10 0 h8" stroke="#f7a100" stroke-width="2" fill="none"/></svg>Service Charge</div>
  <div class="abs module-head" style="top:448px;left:284px"><svg width="22" height="22"><circle cx="11" cy="11" r="10" fill="#f7a100"/><path d="M7 7l8 8M15 7l-8 8" stroke="#fff" stroke-width="2"/></svg>Cosec</div>

  <div class="abs tile" style="top:502px;left:32px">Asbestors<small>NA</small></div>
  <div class="abs tile" style="top:502px;left:118px">Terrorism<small>NA</small></div>
  <div class="abs tile" style="top:502px;left:203px">Year End<small>12/12/2024</small></div>
  <div class="abs tile tile--tall" style="top:502px;left:289px">Are we Responsible?<small>NO</small></div>
  <div class="abs tile" style="top:552px;left:32px">Legionellars<small>-</small></div>
  <div class="abs tile" style="top:552px;left:118px">Terrorism<small>NA</small></div>
  <div class="abs tile" style="top:552px;left:203px">Demand Dates<small>NA</small></div>
  <div class="abs tile" style="top:602px;left:32px">Drains<small>Over10 Dec 2023</small></div>
  <div class="abs tile" style="top:602px;left:118px">Terrorism<small>NA</small></div>
  <div class="abs tile" style="top:652px;left:32px">Gutters<small>NA</small></div>
  <div class="abs tile" style="top:652px;left:118px">Terrorism<small>NA</small></div>
  <div class="abs tile" style="top:702px;left:32px">Dry Risers<small>NA</small></div>
  <div class="abs tile" style="top:702px;left:118px">Terrorism<small>NA</small></div>

  <nav class="abs tabbar">
    <div class="tabbar__item tabbar__item--home"><svg width="22" height="20"><path d="M11 1 L21 10 H18 V19 H4 V10 H1Z" fill="#7a5a1c"/></svg>Home</div>
    <div class="tabbar__item"><svg width="22" height="20"><rect x="3" y="3" width="8" height="17" fill="#fff"/><rect x="12" y="7" width="7" height="13" fill="#fff"/></svg>Overview</div>
    <div class="tabbar__item"><svg width="22" height="20"><circle cx="13" cy="6" r="5" fill="#fff"/><path d="M2 15 q5-3 9 0 h9" stroke="#fff" stroke-width="2.5" fill="none"/></svg>Finances</div>
    <div class="tabbar__item"><svg width="22" height="20"><rect x="2" y="5" width="18" height="12" fill="#fff"/><path d="M2 5l9 7 9-7" stroke="#f7a100" stroke-width="1.5" fill="none"/></svg>Messages</div>
  </nav>
</section>

<!-- Screen 2: finances -->
<section class="screen screen--finances">
  <div class="abs status"><span>12:00</span><span class="status__icons"><svg width="58" height="11"><rect x="0" y="7" width="3" height="4" fill="#111"/><rect x="5" y="5" width="3" height="6" fill="#111"/><rect x="10" y="3" width="3" height="8" fill="#111"/><rect x="15" y="1" width="3" height="10" fill="#111"/><path d="M23 4 q6-5 12 0 M25 7 q4-3 8 0" stroke="#111" stroke-width="1.8" fill="none"/><rect x="38" y="1" width="18" height="9" rx="2" fill="#111"/></svg></span></div>
  <div class="abs brand">HOLMA</div>
  <div class="abs rule"></div>
  <svg class="abs back" width="16" height="14"><path d="M7 1L1 7l6 6M1 7h14" stroke="#111" stroke-width="2.4" fill="none"/></svg>
  <div class="abs page-title">FINANCES</div>

  <div class="abs band" style="top:141px">ACCOUNTS RECEIVABLE</div>
  <div class="abs rows" style="top:168px">
    <div class="row">AREARS<span class="row__amt">$7,268.22</span><span class="row__total">Total</span><span class="row__count">05</span><span class="row__unit">Bils</span></div>
    <div class="row">UNALLOCATED RECIEPTS<span class="row__amt">$7,268.22</span><span class="row__total">Total</span><span class="row__count">05</span><span class="row__unit">Reciepts</span></div>
  </div>
  <div class="abs band" style="top:261px">ACCOUNTS PAYABLE</div>
  <div class="abs rows" style="top:288px">
    <div class="row">INVOICES<span class="row__amt">$4,268.22</span><span class="row__total">Total</span><span class="row__count">05</span><span class="row__unit">Invoices</span></div>
  </div>

  <div class="abs art" role="img" aria-label="Line illustration of people working around a rising growth arrow, a percentage badge and coins"></div>

  <nav class="abs tabbar">
    <div class="tabbar__item tabbar__item--home"><svg width="22" height="20"><path d="M11 1 L21 10 H18 V19 H4 V10 H1Z" fill="#7a5a1c"/></svg>Home</div>
    <div class="tabbar__item"><svg width="22" height="20"><rect x="3" y="3" width="8" height="17" fill="#fff"/><rect x="12" y="7" width="7" height="13" fill="#fff"/></svg>Overview</div>
    <div class="tabbar__item"><svg width="22" height="20"><circle cx="13" cy="6" r="5" fill="#fff"/><path d="M2 15 q5-3 9 0 h9" stroke="#fff" stroke-width="2.5" fill="none"/></svg>Finances</div>
    <div class="tabbar__item"><svg width="22" height="20"><rect x="2" y="5" width="18" height="12" fill="#fff"/><path d="M2 5l9 7 9-7" stroke="#f7a100" stroke-width="1.5" fill="none"/></svg>Messages</div>
  </nav>
</section>

<!-- Screen 3: legionella question -->
<section class="screen screen--legionella">
  <div class="abs status"><span>12:00</span><span class="status__icons"><svg width="58" height="11"><rect x="0" y="7" width="3" height="4" fill="#111"/><rect x="5" y="5" width="3" height="6" fill="#111"/><rect x="10" y="3" width="3" height="8" fill="#111"/><rect x="15" y="1" width="3" height="10" fill="#111"/><path d="M23 4 q6-5 12 0 M25 7 q4-3 8 0" stroke="#111" stroke-width="1.8" fill="none"/><rect x="38" y="1" width="18" height="9" rx="2" fill="#111"/></svg></span></div>
  <div class="abs brand">HOLMA</div>
  <div class="abs rule"></div>
  <svg class="abs back" width="16" height="14"><path d="M7 1L1 7l6 6M1 7h14" stroke="#111" stroke-width="2.4" fill="none"/></svg>
  <div class="abs page-title">LEGIONELLAS</div>

  <div class="abs band" style="top:141px">IS IT REQUIRED?</div>
  <div class="abs rows" style="top:168px">
    <div class="row">NO<span class="check"></span></div>
    <div class="row" style="height:35px">YES BUT I DO NOT HAVE A FILE TO UPLOAD<span class="check"></span></div>
    <div class="row" style="height:39px">YES AND I HAVE A FILE TO UPLOAD<svg class="check" style="border:none;width:11px;height:11px" width="11" height="11"><rect x="0.5" y="0.5" width="9" height="9" fill="none" stroke="#f3b34a"/><path d="M2.5 5l2 2 5-5" stroke="#f7a100" stroke-width="1.5" fill="none"/></svg></div>
  </div>

  <div class="abs btn btn--ghost">« BACK</div>
  <div class="abs btn btn--solid">NEXT »</div>

  <div class="abs art" role="img" aria-label="Isometric illustration of a person with a laptop seated on a large pie chart among charts and data icons"></div>

  <nav class="abs tabbar">
    <div class="tabbar__item tabbar__item--home"><svg width="22" height="20"><path d="M11 1 L21 10 H18 V19 H4 V10 H1Z" fill="#7a5a1c"/></svg>Home</div>
    <div class="tabbar__item"><svg width="22" height="20"><rect x="3" y="3" width="8" height="17" fill="#fff"/><rect x="12" y="7" width="7" height="13" fill="#fff"/></svg>Overview</div>
    <div class="tabbar__item"><svg width="22" height="20"><circle cx="13" cy="6" r="5" fill="#fff"/><path d="M2 15 q5-3 9 0 h9" stroke="#fff" stroke-width="2.5" fill="none"/></svg>Finances</div>
    <div class="tabbar__item"><svg width="22" height="20"><rect x="2" y="5" width="18" height="12" fill="#fff"/><path d="M2 5l9 7 9-7" stroke="#f7a100" stroke-width="1.5" fill="none"/></svg>Messages</div>
  </nav>
</section>

</body>
</html>
```